Very High End Grooming Salon needs new business card design

I need a very nice card design I am a certified Master groomer we have a very high end clients. Our color is pink but does not have to be pink. I have a logo also a mission statement .
Fern N Fluff Pet Boutique and Spa
48710 Orchard Rd
Cedar Glen fl 33921
561 904 3826
www.fernfluffboutique-example.com
online booking available
this is our mission statement not sure it need to go on card but here it is.
Our Mission is to show respect to all animals pampering them with the same high end tailored service one would expect to receive at a day spa
as the only certified master groomer in the area we strive to put your pets best paw forward.

Industry/Entity Type

Business

```html
<!DOCTYPE html>
<html lang="en">
<head>
<meta charset="utf-8">
<title>Fern N Fluff Pet Boutique and Spa – Business Card</title>
<link rel="stylesheet" href="https://fonts.googleapis.com/css2?family=Arimo:wght@400&display=swap">
<style>
  :root {
    --backdrop: #e9e4e1;
    --card: #ffffff;
    --magenta: #d7318f;
    --blush: #f1c3dc;
    --ink-pink: #d8358f;
    --ink-soft: #e27ab5;
    --ink-grey: #b5b1b3;
  }
  * { margin: 0; padding: 0; box-sizing: border-box; }
  html, body {
    width: 1200px; height: 858px; overflow: hidden;
    background: var(--backdrop);
    font-family: "Arimo", Arial, sans-serif;
  }
  .sheet {
    width: 1200px; height: 858px;
    display: flex; flex-direction: column;
    align-items: center; justify-content: center; gap: 36px;
  }
  .card {
    position: relative;
    width: 660px; height: 377px;
    background: var(--card);
    overflow: hidden;
    box-shadow: 0 6px 18px rgba(0,0,0,.12);
  }
  .band-soft, .band-strong { position: absolute; top: 0; bottom: 0; }
  .band-soft { width: 62px; background: linear-gradient(90deg, #f8e1ee, var(--blush)); }
  .band-strong { width: 40px; background: var(--magenta); }

  /* front */
  .card--front .band-soft { right: 50px; }
  .card--front .band-strong { right: 0; }
  .person { position: absolute; left: 48px; top: 70px; }
  .person__name { font-size: 27px; color: var(--ink-pink); }
  .person__title { font-size: 17px; color: var(--ink-grey); margin-top: 6px; margin-left: 2px; }
  .contact {
    position: absolute; left: 48px; bottom: 56px;
    list-style: none; font-size: 17px; color: var(--ink-soft); line-height: 1.55;
  }
  .contact li { display: flex; align-items: flex-start; gap: 12px; }
  .contact svg { width: 15px; height: 15px; margin-top: 5px; flex: none; fill: var(--ink-soft); }
  .contact .blank { width: 15px; flex: none; }

  /* back */
  .card--back .band-strong { left: 0; }
  .card--back .band-soft { left: 50px; background: linear-gradient(270deg, #f8e1ee, var(--blush)); }
  .brand {
    position: absolute; left: 150px; right: 40px; top: 0; bottom: 0;
    display: flex; flex-direction: column; align-items: center; justify-content: center; gap: 14px;
  }
  .brand__row { display: flex; align-items: center; gap: 14px; }
  .brand__dot { width: 22px; height: 22px; border-radius: 50%; background: var(--blush); }
  .brand__name { color: var(--ink-pink); font-size: 34px; }
  .brand__tag { color: var(--ink-pink); font-size: 16px; letter-spacing: 3px; text-transform: uppercase; }
</style>
</head>
<body>
<main class="sheet">
  <section class="card card--front" aria-label="Card front">
    <div class="person">
      <p class="person__name">Employee Name</p>
      <p class="person__title">Title</p>
    </div>
    <ul class="contact">
      <li>
        <svg viewBox="0 0 16 16" aria-hidden="true"><path d="M3 1h3l1.5 4-2 1.2a9 9 0 0 0 4.3 4.3L11 8.5l4 1.5v3c0 1-1 2-2 2C6.4 15 1 9.6 1 3c0-1 1-2 2-2z"/></svg>
        <span>561 904 3826</span>
      </li>
      <li>
        <svg viewBox="0 0 16 16" aria-hidden="true"><circle cx="8" cy="8" r="7" fill="none" style="stroke:var(--ink-soft)" stroke-width="1.6"/><path d="M1 8h14M8 1c-3 4-3 10 0 14M8 1c3 4 3 10 0 14" fill="none" style="stroke:var(--ink-soft)" stroke-width="1.2"/></svg>
        <span>www.fernfluffboutique-example.com</span>
      </li>
      <li>
        <svg viewBox="0 0 16 16" aria-hidden="true"><path d="M8 0a5.5 5.5 0 0 0-5.5 5.5C2.5 10 8 16 8 16s5.5-6 5.5-10.5A5.5 5.5 0 0 0 8 0zm0 8a2.5 2.5 0 1 1 0-5 2.5 2.5 0 0 1 0 5z"/></svg>
        <span>48710 Orchard Rd</span>
      </li>
      <li><span class="blank"></span><span>Cedar Glen fl 33921</span></li>
    </ul>
    <div class="band-soft"></div>
    <div class="band-strong"></div>
  </section>

  <section class="card card--back" aria-label="Card back">
    <div class="band-strong"></div>
    <div class="band-soft"></div>
    <div class="brand">
      <div class="brand__row">
        <span class="brand__dot" aria-hidden="true"></span>
        <span class="brand__name">Fern N Fluff</span>
      </div>
      <span class="brand__tag">Pet Boutique and Spa</span>
    </div>
  </section>
</main>
</body>
</html>
```